PPT template for boutique strategic planning, accounting and taxation firm

We are a boutique firm that provides strategic, accounting and tax advice to our clients. The work we are doing is increasingly strategic work and we are required to produce reports and presentations and our current templates are simply not sufficient.
As you can see from the examples attached, we have very limited skills in house re design! We have attached a PPT document and word document (that should be PPT) that we use regularly as examples of the content. Excel worksheets are regularly embedded into the presentation (in both blue and orange - see below re colours)
Not specific to one area but typically these clients are famous for their own brand and are creating value in their industry through creating their own brand and we want to produce documents of a similar standard.
A Powerpoint Document Slide Template
Cover page layout, back page, intermediate page heading, in colours and styles based on the logo, title styles, and an intermediate or chapter heading slide style. Many of our presentations contain slides with tables, diagrams, flowcharts and text, including simple lists of bullet points. As above, you will see in our style guide that we have three coloured logos – we would like one version in blue and one version in orange please. Again, the cover should be bold and draw attention but remain professional.
We are looking for something that works in both 4:3 and 16:9 (or two templates please)
We like a clear professional and simple look.
Deliverable: PowerPoint template file (.potx extension) for PowerPoint 2007 with at least a “cover” layout, a “title and content” layout, and a simplified slide layout, as well as “back cover”. Please embed any fonts used.
Target Market(s)
Many of our clients are retail clients or have strong brands of their own.
Industry/Entity Type
Accounting
Requirements
Must have
- Harrowby & Co logo on each page.
Must have a cover page (please be bold but professional)
A selection of "standard" slides - dot points, detailed written content, example diagrams, flow charts etc.
A back cover
Nice to have
- We would like to have a copy done in both the blue and orange versions attached. Happy for the winner to complete the other colour after the winner is selected.
Prefer Arial logo but open to suggestions. Must be easy to read and professional
Should not have
- Nothing cartoonish

```html
<!DOCTYPE html>
<html lang="en">
<head>
<meta charset="utf-8">
<title>Harrowby &amp; Co – Presentation Template</title>
<link href="https://fonts.googleapis.com/css2?family=Open+Sans:wght@400;600;700;800&display=swap" rel="stylesheet">
<style>
:root{
  --page:#000;
  --blue:#1f6fc1;
  --blue-dark:#0f4f9e;
  --blue-light:#39a5e6;
  --navy:#143e74;
  --ink:#1c1c1c;
  --body:#333;
  --grey:#8a8a8a;
  --yellow:#ffd200;
}
*{box-sizing:border-box;margin:0;padding:0}
html,body{width:932px;height:1200px;overflow:hidden;background:var(--page)}
body{position:relative;font-family:'Open Sans',Arial,sans-serif}
.slide{position:absolute;width:293px;height:223px;background:#fff;overflow:hidden}
.c1{left:10px}.c2{left:320px}.c3{left:629px}
.r1{top:10px}.r2{top:250px}.r3{top:490px}.r4{top:728px}.r5{top:967px}
.top-accent{position:absolute;left:0;top:0;width:92px;height:2px;background:var(--blue)}
.slide-title{position:absolute;left:33px;top:16px;font-weight:800;font-size:7.4px;color:var(--ink);letter-spacing:.1px;white-space:nowrap}
.body-text{position:absolute;font-size:3.9px;line-height:1.45;color:var(--body);text-align:justify}
.body-text p+p{margin-top:4px}
.footer{position:absolute;left:0;bottom:0;width:293px;height:42px}
.footer svg{position:absolute;inset:0}
.footer-url{position:absolute;left:18px;bottom:8px;font-size:3.4px;color:#dbe9f8}
.footer-num{position:absolute;right:12px;bottom:8px;font-size:3.4px;color:#dbe9f8}
.footer-brand{position:absolute;left:0;right:0;bottom:6px;display:flex;justify-content:center;align-items:center;gap:3px}
.brand-mark{width:6px;height:6px;background:#fff}
.brand-name{font-weight:700;font-size:6.5px;color:#fff;letter-spacing:.2px}
.photo{position:absolute;border-radius:1px}
.cover-bg{position:absolute;inset:0}
.cover-logo{position:absolute;left:0;right:0;display:flex;flex-direction:column;align-items:center}
.cover-logo .row{display:flex;align-items:center;gap:4px}
.cover-logo .mark{background:var(--ink)}
.cover-logo .name{font-weight:700;color:var(--ink);letter-spacing:.3px}
.cover-logo .tag{font-size:3.3px;color:var(--ink);margin-top:2px;font-weight:400;letter-spacing:.4px}
.cover-logo.light .mark{background:#fff}
.cover-logo.light .name,.cover-logo.light .tag{color:#fff}
.cover-title{position:absolute;left:0;right:0;text-align:center;font-weight:800;color:#fff;font-size:12.5px}
.cover-sub{position:absolute;left:0;right:0;text-align:center;font-weight:700;color:var(--yellow);font-size:6px}
.cover-url{position:absolute;left:0;right:0;bottom:14px;text-align:center;font-size:4px;color:var(--ink)}
.num{position:absolute;width:13px;height:13px;border-radius:50%;background:var(--blue-light);color:#fff;font-size:4.5px;font-weight:700;display:flex;align-items:center;justify-content:center}
.item-head{position:absolute;font-size:4.6px;font-weight:800;color:var(--ink);padding-bottom:2px;border-bottom:.6px solid var(--blue-light)}
.item-text{position:absolute;font-size:3.8px;line-height:1.45;color:var(--body)}
.bullets{position:absolute;left:168px;top:44px;list-style:none}
.bullets li{font-size:3.9px;color:var(--body);height:10.4px;display:flex;align-items:center;gap:5px}
.bullets li::before{content:"";width:3.4px;height:3.4px;border:.5px solid var(--blue-light);border-radius:50%}
.data-table{position:absolute;border-collapse:collapse}
.data-table td{border:.6px solid #fff;height:9.2px;background:#d9d9d9}
.data-table tr:nth-child(even) td{background:#c4c4c4}
.data-table tr:first-child td{background:#8c8c8c;height:13px}
.legend{position:absolute;display:flex;gap:5px;font-size:3px;color:#555;white-space:nowrap}
.legend span::before{content:"";display:inline-block;width:2.5px;height:2.5px;margin-right:1px;background:var(--blue-light)}
</style>
</head>
<body>

<section class="slide c1 r1" style="background:radial-gradient(circle at 50% 50%,#fff 0%,#f1f1f1 55%,#d9d9d9 100%)">
  <div class="cover-logo" style="top:96px">
    <div class="row"><span class="mark" style="width:11px;height:11px"></span><span class="name" style="font-size:13px">Harrowby &amp; Co</span></div>
    <div class="tag">Strategy, Accounts &amp; Tax Advice</div>
  </div>
</section>

<section class="slide c2 r1">
  <svg class="cover-bg" viewBox="0 0 293 223" aria-hidden="true">
    <defs>
      <linearGradient id="gGrey" x1="0" y1="0" x2="0" y2="1"><stop offset="0" stop-color="#d6d6d6"/><stop offset="1" stop-color="#fafafa"/></linearGradient>
      <linearGradient id="gBand" x1="0" y1="0" x2="1" y2="0"><stop offset="0" stop-color="#0d4c9c"/><stop offset=".5" stop-color="#2e8de0"/><stop offset="1" stop-color="#0d4c9c"/></linearGradient>
      <linearGradient id="gShade" x1="0" y1="0" x2="0" y2="1"><stop offset="0" stop-color="#fff" stop-opacity=".35"/><stop offset=".4" stop-color="#fff" stop-opacity="0"/></linearGradient>
    </defs>
    <rect width="293" height="223" fill="url(#gGrey)"/>
    <path d="M0 62 Q146 50 293 62 V150 L146 186 L0 150Z" fill="url(#gBand)"/>
    <path d="M0 62 Q146 50 293 62 V150 L146 186 L0 150Z" fill="url(#gShade)"/>
    <path d="M0 150 L146 186 L293 150" fill="none" stroke="#9fd0f5" stroke-width="1"/>
  </svg>
  <div class="cover-logo" style="top:22px">
    <div class="row"><span class="mark" style="width:7px;height:7px"></span><span class="name" style="font-size:8px">Harrowby &amp; Co</span></div>
    <div class="tag" style="font-size:2.8px">Strategy, Accounts &amp; Tax Advice</div>
  </div>
  <div class="cover-title" style="top:98px">PRESENTATION TITTLE HERE</div>
  <div class="cover-sub" style="top:117px">YOUR PRESENTATION TITLE HERE</div>
  <div class="cover-url">www.harrowbyco.com</div>
</section>

<section class="slide c3 r1">
  <div class="top-accent"></div>
  <div class="slide-title">CONCEPT PLUS PRESENTATION POWERFUL MISSION 1</div>
  <div class="photo" role="img" aria-label="Photograph of a lit office tower at dusk" style="left:31px;top:36px;width:110px;height:148px;background:linear-gradient(180deg,#5d7896 0%,#2c3b52 55%,#1a2230 100%)"></div>
  <div class="body-text" style="left:150px;top:36px;width:112px">
    <p>Our firm has built a calm and steady approach to strategy, accounts and tax. By clearing old hurdles that held growing brands back, we help owners plan the next stage with confidence.</p>
    <p>Central to this approach are four steps that move each client forward. We review the numbers, shape a plan, test it with the team and report clearly. With these steps, clients can act sooner.</p>
    <p>Practical advice that has changed how our clients plan, report and grow is at the heart of our work.</p>
  </div>
  <div class="footer"><svg viewBox="0 0 293 42" preserveAspectRatio="none" aria-hidden="true"><defs><linearGradient id="fb" x1="0" y1="0" x2="1" y2="0"><stop offset="0" stop-color="#0d4c9c"/><stop offset=".5" stop-color="#3b9be6"/><stop offset="1" stop-color="#0d4c9c"/></linearGradient></defs><rect y="8" width="293" height="34" fill="url(#fb)"/><path d="M0 0 H293 V10 Q220 14 146 24 Q73 14 0 10Z" fill="#fff"/><path d="M0 10 Q73 14 146 24 Q220 14 293 10" fill="none" stroke="#a9d6f7" stroke-width=".8"/></svg><span class="footer-url">www.harrowbyco.com</span><div class="footer-brand"><span class="brand-mark"></span><span class="brand-name">Harrowby &amp; Co</span></div><span class="footer-num">3</span></div>
</section>

<section class="slide c1 r2">
  <div class="top-accent"></div>
  <div class="slide-title">CONCEPT PLUS PRESENTATION POWERFUL MISSION 2</div>
  <div class="photo" role="img" aria-label="Photograph of a smiling business team" style="left:35px;top:52px;width:80px;height:50px;background:linear-gradient(135deg,#cbb9a6 0%,#6d5a4a 55%,#e9e4dd 100%)"></div>
  <div class="body-text" style="left:35px;top:110px;width:80px">
    <p>Our firm has built a calm and steady approach to strategy, accounts and tax work.</p>
    <p>By clearing old hurdles that held growing brands back, we help owners plan the next stage. Practical advice has changed how our clients plan and grow.</p>
  </div>
  <div class="body-text" style="left:152px;top:52px;width:112px">
    <p>Our firm has built a calm and steady approach to strategy, accounts and tax. By clearing old hurdles that held growing brands back, we help owners plan ahead.</p>
    <p>Central to this approach are four steps that move each client forward. We review the numbers, shape a plan, test it with the team and report clearly. With these steps, clients can act sooner.</p>
    <p>Practical advice that has changed how our clients plan is at the heart of our work.</p>
  </div>
  <div class="footer"><svg viewBox="0 0 293 42" preserveAspectRatio="none" aria-hidden="true"><rect y="8" width="293" height="34" fill="url(#fb)"/><path d="M0 0 H293 V10 Q220 14 146 24 Q73 14 0 10Z" fill="#fff"/><path d="M0 10 Q73 14 146 24 Q220 14 293 10" fill="none" stroke="#a9d6f7" stroke-width=".8"/></svg><span class="footer-url">www.harrowbyco.com</span><div class="footer-brand"><span class="brand-mark"></span><span class="brand-name">Harrowby &amp; Co</span></div><span class="footer-num">2</span></div>
</section>

<section class="slide c2 r2">
  <div class="top-accent"></div>
  <div class="slide-title">CONCEPT PLUS PRESENTATION POWERFUL MISSION 3</div>
  <span class="num" style="left:31px;top:53px">1</span>
  <div class="item-head" style="left:56px;top:51px;width:205px">WE KNOW FIRSTHAND 1</div>
  <div class="item-text" style="left:56px;top:63px;width:205px">Since 1998, we have guided many owners from first review to final plan, clearing hurdles that held their business back and taking their brand to a new level.</div>
  <span class="num" style="left:31px;top:95px">2</span>
  <div class="item-head" style="left:56px;top:93px;width:205px">WE KNOW FIRSTHAND 2</div>
  <div class="item-text" style="left:56px;top:105px;width:205px">Since 1998, we have guided many owners from first review to final plan, clearing hurdles that held their business back and taking their brand to a new level.</div>
  <span class="num" style="left:31px;top:137px">3</span>
  <div class="item-head" style="left:56px;top:135px;width:205px">WE KNOW FIRSTHAND 3</div>
  <div class="item-text" style="left:56px;top:147px;width:205px">Since 1998, we have guided many owners from first review to final plan, clearing hurdles that held their business back and taking their brand to a new level.</div>
  <div class="footer"><svg viewBox="0 0 293 42" preserveAspectRatio="none" aria-hidden="true"><rect y="8" width="293" height="34" fill="url(#fb)"/><path d="M0 0 H293 V10 Q220 14 146 24 Q73 14 0 10Z" fill="#fff"/><path d="M0 10 Q73 14 146 24 Q220 14 293 10" fill="none" stroke="#a9d6f7" stroke-width=".8"/></svg><span class="footer-url">www.harrowbyco.com</span><div class="footer-brand"><span class="brand-mark"></span><span class="brand-name">Harrowby &amp; Co</span></div><span class="footer-num">3</span></div>
</section>

<section class="slide c3 r2">
  <div class="top-accent"></div>
  <div class="slide-title">CONCEPT PLUS PRESENTATION POWERFUL MISSION 4</div>
  <span class="num" style="left:31px;top:53px">1</span>
  <div class="item-head" style="left:56px;top:51px;width:85px">WE KNOW FIRSTHAND 1</div>
  <div class="item-text" style="left:56px;top:63px;width:85px">Since 1998, we have guided many owners from the first review.</div>
  <span class="num" style="left:31px;top:86px">2</span>
  <div class="item-head" style="left:56px;top:84px;width:85px">WE KNOW FIRSTHAND 2</div>
  <div class="item-text" style="left:56px;top:96px;width:85px">Since 1998, we have guided many owners from first review to final plan, clearing hurdles that held their business back.</div>
  <span class="num" style="left:31px;top:134px">3</span>
  <div class="item-head" style="left:56px;top:132px;width:85px">WE KNOW FIRSTHAND 3</div>
  <div class="item-text" style="left:56px;top:144px;width:85px">Since 1998, we have guided many owners from first review to a clear plan for their brand.</div>
  <span class="num" style="left:148px;top:53px">4</span>
  <div class="item-head" style="left:173px;top:51px;width:85px">WE KNOW FIRSTHAND 4</div>
  <div class="item-text" style="left:173px;top:63px;width:85px">Since 1998, we have guided many owners from the first review.</div>
  <span class="num" style="left:148px;top:86px">5</span>
  <div class="item-head" style="left:173px;top:84px;width:85px">WE KNOW FIRSTHAND 5</div>
  <div class="item-text" style="left:173px;top:96px;width:85px">Since 1998, we have guided many owners from first review to final plan, clearing hurdles that held their business back.</div>
  <span class="num" style="left:148px;top:134px">6</span>
  <div class="item-head" style="left:173px;top:132px;width:85px">WE KNOW FIRSTHAND 6</div>
  <div class="item-text" style="left:173px;top:144px;width:85px">Since 1998, we have guided many owners from first review to a clear plan for their brand.</div>
  <div class="footer"><svg viewBox="0 0 293 42" preserveAspectRatio="none" aria-hidden="true"><rect y="8" width="293" height="34" fill="url(#fb)"/><path d="M0 0 H293 V10 Q220 14 146 24 Q73 14 0 10Z" fill="#fff"/><path d="M0 10 Q73 14 146 24 Q220 14 293 10" fill="none" stroke="#a9d6f7" stroke-width=".8"/></svg><span class="footer-url">www.harrowbyco.com</span><div class="footer-brand"><span class="brand-mark"></span><span class="brand-name">Harrowby &amp; Co</span></div><span class="footer-num">4</span></div>
</section>

<section class="slide c1 r3">
  <div class="top-accent"></div>
  <div class="slide-title">MORE THAN 500+ SATISFIED CLIENT OVER THE WORLD</div>
  <div class="photo" role="img" aria-label="Grey world map with client counts and people markers per region" style="left:28px;top:38px;width:240px;height:132px;border-radius:10px;background:radial-gradient(ellipse at 50% 50%,#bdbdbd 0%,#cfcfcf 60%,#fff 100%)"></div>
  <div class="footer"><svg viewBox="0 0 293 42" preserveAspectRatio="none" aria-hidden="true"><rect y="8" width="293" height="34" fill="url(#fb)"/><path d="M0 0 H293 V10 Q220 14 146 24 Q73 14 0 10Z" fill="#fff"/><path d="M0 10 Q73 14 146 24 Q220 14 293 10" fill="none" stroke="#a9d6f7" stroke-width=".8"/></svg><span class="footer-url">www.harrowbyco.com</span><div class="footer-brand"><span class="brand-mark"></span><span class="brand-name">Harrowby &amp; Co</span></div><span class="footer-num">5</span></div>
</section>

<section class="slide c2 r3">
  <svg class="cover-bg" viewBox="0 0 293 223" aria-hidden="true">
    <defs>
      <radialGradient id="gDiv" cx=".5" cy=".55" r=".7"><stop offset="0" stop-color="#8fd2fa"/><stop offset=".45" stop-color="#3a9ae3"/><stop offset="1" stop-color="#0f5aa9"/></radialGradient>
    </defs>
    <rect width="293" height="223" fill="#f2f2f2"/>
    <path d="M0 0 H293 V150 L146 186 L0 150Z" fill="url(#gDiv)"/>
    <path d="M0 150 L146 186 L293 150" fill="none" stroke="#cdeafc" stroke-width="1"/>
  </svg>
  <div class="cover-logo light" style="top:22px">
    <div class="row"><span class="mark" style="width:7px;height:7px"></span><span class="name" style="font-size:8px">Harrowby &amp; Co</span></div>
    <div class="tag" style="font-size:2.8px">Strategy, Accounts &amp; Tax Advice</div>
  </div>
  <div class="cover-title" style="top:96px">DIVIDER PAGES HERE</div>
  <div class="cover-sub" style="top:115px;color:var(--navy)">YOUR PRESENTATION TITLE HERE</div>
  <div class="cover-url">www.harrowbyco.com</div>
</section>

<section class="slide c3 r3">
  <div class="top-accent"></div>
  <div class="slide-title">CONCEPT PLUS PRESENTATION POWERFUL MISSION 5</div>
  <svg style="position:absolute;left:0;top:0" width="293" height="120" viewBox="0 0 293 120" aria-label="Process: brief, analiser, design, develop, testing">
    <defs>
      <linearGradient id="cB1" x1="0" y1="0" x2="0" y2="1"><stop offset="0" stop-color="#5bb8f0"/><stop offset="1" stop-color="#1a78c8"/></linearGradient>
      <linearGradient id="cB2" x1="0" y1="0" x2="0" y2="1"><stop offset="0" stop-color="#7cc9f4"/><stop offset="1" stop-color="#2e95dc"/></linearGradient>
      <linearGradient id="cG1" x1="0" y1="0" x2="0" y2="1"><stop offset="0" stop-color="#b3b3b3"/><stop offset="1" stop-color="#6b6b6b"/></linearGradient>
      <linearGradient id="cG2" x1="0" y1="0" x2="0" y2="1"><stop offset="0" stop-color="#8c8c8c"/><stop offset="1" stop-color="#4a4a4a"/></linearGradient>
    </defs>
    <circle cx="228" cy="80" r="23" fill="url(#cG2)" stroke="#fff" stroke-width="1.2"/>
    <circle cx="183" cy="80" r="23" fill="url(#cG1)" stroke="#fff" stroke-width="1.2"/>
    <circle cx="137" cy="80" r="23" fill="url(#cB2)" stroke="#fff" stroke-width="1.2"/>
    <circle cx="91" cy="80" r="23" fill="url(#cB1)" stroke="#fff" stroke-width="1.2"/>
    <circle cx="45" cy="80" r="23" fill="url(#cB1)" stroke="#fff" stroke-width="1.2"/>
    <g fill="#fff" font-family="Open Sans, Arial, sans-serif" font-size="4.2" font-weight="700" text-anchor="middle">
      <text x="45" y="81.5">BRIEF</text><text x="91" y="81.5">ANALISER</text><text x="137" y="81.5">DESIGN</text><text x="183" y="81.5">DEVELOP</text><text x="228" y="81.5">TESTING</text>
    </g>
  </svg>
  <div class="body-text" style="left:33px;top:120px;width:228px">
    <p>The pace at which our planning approach helps owners review their results, clearing hurdles that held the brand back.</p>
    <p>We have taken many growing firms to a new level, and fresh plans can be brought to each client sooner. By clearing old hurdles that held the business back, our team can quickly turn clear numbers into sound decisions for every brand we serve.</p>
  </div>
  <div class="footer"><svg viewBox="0 0 293 42" preserveAspectRatio="none" aria-hidden="true"><rect y="8" width="293" height="34" fill="url(#fb)"/><path d="M0 0 H293 V10 Q220 14 146 24 Q73 14 0 10Z" fill="#fff"/><path d="M0 10 Q73 14 146 24 Q220 14 293 10" fill="none" stroke="#a9d6f7" stroke-width=".8"/></svg><span class="footer-url">www.harrowbyco.com</span><div class="footer-brand"><span class="brand-mark"></span><span class="brand-name">Harrowby &amp; Co</span></div><span class="footer-num">7</span></div>
</section>

<section class="slide c1 r4">
  <div class="top-accent"></div>
  <div class="slide-title">CONCEPT PLUS PRESENTATION POWERFUL MISSION 6</div>
  <svg style="position:absolute;left:0;top:0" width="160" height="180" viewBox="0 0 160 180" aria-label="Nested stages: brief, analiser, design, develop, testing">
    <defs>
      <linearGradient id="nG" x1="0" y1="0" x2="0" y2="1"><stop offset="0" stop-color="#8f8f8f"/><stop offset="1" stop-color="#dcdcdc"/></linearGradient>
      <linearGradient id="nG2" x1="0" y1="0" x2="0" y2="1"><stop offset="0" stop-color="#b0b0b0"/><stop offset="1" stop-color="#eeeeee"/></linearGradient>
      <linearGradient id="nB" x1="0" y1="0" x2="0" y2="1"><stop offset="0" stop-color="#1f82d0"/><stop offset="1" stop-color="#6cc3f3"/></linearGradient>
      <linearGradient id="nB2" x1="0" y1="0" x2="0" y2="1"><stop offset="0" stop-color="#2f97e0"/><stop offset="1" stop-color="#8ad3f7"/></linearGradient>
    </defs>
    <circle cx="78" cy="104" r="55" fill="url(#nG)" stroke="#fff" stroke-width="1"/>
    <circle cx="78" cy="114" r="45" fill="url(#nG2)" stroke="#fff" stroke-width="1"/>
    <circle cx="78" cy="124" r="35" fill="url(#nB)" stroke="#fff" stroke-width="1"/>
    <circle cx="78" cy="134" r="25" fill="url(#nB2)" stroke="#fff" stroke-width="1"/>
    <circle cx="78" cy="144" r="15" fill="#4cb0ec" stroke="#fff" stroke-width="1"/>
    <g fill="#fff" font-family="Open Sans, Arial, sans-serif" font-size="4.4" font-weight="700" text-anchor="middle">
      <text x="78" y="61">BRIEF</text><text x="78" y="80.5">ANALISER</text><text x="78" y="100.5">DESIGN</text><text x="78" y="121.5">DEVELOP</text><text x="78" y="146">TESTING</text>
    </g>
  </svg>
  <ul class="bullets">
    <li>Since 1998, we have guided</li><li>Central to this approach</li><li>Hurdles that held it back</li><li>Since 1998, we have guided</li><li>Central to this approach</li><li>Hurdles that held it back</li><li>Plans that lift the brand</li><li>Clear reporting for owners</li><li>Since 1998, we have guided</li><li>Central to this approach</li><li>Hurdles that held it back</li>
  </ul>
  <div class="footer"><svg viewBox="0 0 293 42" preserveAspectRatio="none" aria-hidden="true"><rect y="8" width="293" height="34" fill="url(#fb)"/><path d="M0 0 H293 V10 Q220 14 146 24 Q73 14 0 10Z" fill="#fff"/><path d="M0 10 Q73 14 146 24 Q220 14 293 10" fill="none" stroke="#a9d6f7" stroke-width=".8"/></svg><span class="footer-url">www.harrowbyco.com</span><div class="footer-brand"><span class="brand-mark"></span><span class="brand-name">Harrowby &amp; Co</span></div><span class="footer-num">8</span></div>
</section>

<section class="slide c2 r4">
  <div class="top-accent"></div>
  <div class="slide-title">CONCEPT PLUS PRESENTATION POWERFUL MISSION 7</div>
  <div class="body-text" style="left:33px;top:52px;width:102px">
    <p>Our firm has built a calm and steady approach to strategy, accounts and tax. By clearing old hurdles that held growing brands back, we help owners plan ahead.</p>
    <p>Central to this approach are four steps that move each client forward. We review the numbers, shape a plan, test it with the team and report clearly. With these steps, clients can act sooner and grow with confidence.</p>
  </div>
  <svg style="position:absolute;left:140px;top:48px" width="130" height="100" viewBox="0 0 130 100" aria-label="Pie chart">
    <ellipse cx="65" cy="57" rx="58" ry="36" fill="#0e6bb8"/>
    <rect x="7" y="45" width="116" height="12" fill="#0e6bb8"/>
    <path d="M65 45 L65 9 A58 36 0 1 1 9 54 Z" fill="#2f9be6"/>
    <path d="M65 45 L9 54 A58 36 0 0 1 22 22 Z" fill="#7e7e7e"/>
    <path d="M65 45 L22 22 A58 36 0 0 1 65 9 Z" fill="#5a5a5a"/>
  </svg>
  <div class="legend" style="left:150px;top:160px"><span>Pie Chart 1</span><span>Pie Chart 2</span><span>Pie Chart 3</span><span>Pie Chart 4</span></div>
  <div class="footer"><svg viewBox="0 0 293 42" preserveAspectRatio="none" aria-hidden="true"><rect y="8" width="293" height="34" fill="url(#fb)"/><path d="M0 0 H293 V10 Q220 14 146 24 Q73 14 0 10Z" fill="#fff"/><path d="M0 10 Q73 14 146 24 Q220 14 293 10" fill="none" stroke="#a9d6f7" stroke-width=".8"/></svg><span class="footer-url">www.harrowbyco.com</span><div class="footer-brand"><span class="brand-mark"></span><span class="brand-name">Harrowby &amp; Co</span></div><span class="footer-num">9</span></div>
</section>

<section class="slide c3 r4">
  <div class="top-accent"></div>
  <div class="slide-title">CONCEPT PLUS PRESENTATION POWERFUL MISSION 8</div>
  <div class="body-text" style="left:33px;top:52px;width:102px">
    <p>Our firm has built a calm and steady approach to strategy, accounts and tax. By clearing old hurdles that held growing brands back, we help owners plan ahead.</p>
    <p>Central to this approach are four steps that move each client forward. We review the numbers, shape a plan, test it with the team and report clearly. With these steps, clients can act sooner and grow with confidence.</p>
  </div>
  <svg style="position:absolute;left:140px;top:50px" width="130" height="110" viewBox="0 0 130 110" aria-label="Bar chart">
    <defs>
      <linearGradient id="bg1" x1="0" y1="0" x2="1" y2="0"><stop offset="0" stop-color="#6d6d6d"/><stop offset="1" stop-color="#a8a8a8"/></linearGradient>
      <linearGradient id="bb1" x1="0" y1="0" x2="1" y2="0"><stop offset="0" stop-color="#1565b3"/><stop offset="1" stop-color="#4fb2ee"/></linearGradient>
    </defs>
    <rect x="10" y="72" width="20" height="30" fill="url(#bg1)"/><path d="M10 72 l6 -5 h20 l-6 5z" fill="#c4c4c4"/><path d="M30 72 l6 -5 v30 l-6 5z" fill="#555"/>
    <rect x="32" y="58" width="20" height="44" fill="url(#bg1)"/><path d="M32 58 l6 -5 h20 l-6 5z" fill="#c4c4c4"/><path d="M52 58 l6 -5 v44 l-6 5z" fill="#555"/>
    <rect x="54" y="38" width="20" height="64" fill="url(#bb1)"/><path d="M54 38 l6 -5 h20 l-6 5z" fill="#8fd2fa"/><path d="M74 38 l6 -5 v64 l-6 5z" fill="#0e4f95"/>
    <rect x="76" y="14" width="20" height="88" fill="url(#bb1)"/><path d="M76 14 l6 -5 h20 l-6 5z" fill="#8fd2fa"/><path d="M96 14 l6 -5 v88 l-6 5z" fill="#0e4f95"/>
  </svg>
  <div class="legend" style="left:148px;top:163px"><span>Bar Chart 1</span><span>Bar Chart 2</span><span>Bar Chart 3</span><span>Bar Chart 4</span></div>
  <div class="footer"><svg viewBox="0 0 293 42" preserveAspectRatio="none" aria-hidden="true"><rect y="8" width="293" height="34" fill="url(#fb)"/><path d="M0 0 H293 V10 Q220 14 146 24 Q73 14 0 10Z" fill="#fff"/><path d="M0 10 Q73 14 146 24 Q220 14 293 10" fill="none" stroke="#a9d6f7" stroke-width=".8"/></svg><span class="footer-url">www.harrowbyco.com</span><div class="footer-brand"><span class="brand-mark"></span><span class="brand-name">Harrowby &amp; Co</span></div><span class="footer-num">10</span></div>
</section>

<section class="slide c1 r5">
  <div class="top-accent"></div>
  <div class="slide-title">CONCEPT PLUS PRESENTATION POWERFUL MISSION 9</div>
  <div class="body-text" style="left:33px;top:56px;width:95px">
    <p>Our firm has built a calm and steady approach to strategy, accounts and tax. By clearing old hurdles that held growing brands back, we help owners plan ahead.</p>
    <p>Central to this approach are four steps that move each client forward. We review the numbers, shape a plan, test it with the team and report clearly. With these steps, clients can act sooner and grow with confidence.</p>
  </div>
  <table class="data-table" style="left:134px;top:50px;width:128px" aria-label="Data table">
    <tr><td></td><td></td><td></td><td></td></tr><tr><td></td><td></td><td></td><td></td></tr><tr><td></td><td></td><td></td><td></td></tr><tr><td></td><td></td><td></td><td></td></tr><tr><td></td><td></td><td></td><td></td></tr><tr><td></td><td></td><td></td><td></td></tr><tr><td></td><td></td><td></td><td></td></tr><tr><td></td><td></td><td></td><td></td></tr><tr><td></td><td></td><td></td><td></td></tr>
  </table>
  <div class="footer"><svg viewBox="0 0 293 42" preserveAspectRatio="none" aria-hidden="true"><rect y="8" width="293" height="34" fill="url(#fb)"/><path d="M0 0 H293 V10 Q220 14 146 24 Q73 14 0 10Z" fill="#fff"/><path d="M0 10 Q73 14 146 24 Q220 14 293 10" fill="none" stroke="#a9d6f7" stroke-width=".8"/></svg><span class="footer-url">www.harrowbyco.com</span><div class="footer-brand"><span class="brand-mark"></span><span class="brand-name">Harrowby &amp; Co</span></div><span class="footer-num">11</span></div>
</section>

<section class="slide c2 r5">
  <div class="top-accent"></div>
  <div class="slide-title">CONCEPT PLUS PRESENTATION POWERFUL MISSION 10</div>
  <table class="data-table" style="left:33px;top:50px;width:228px" aria-label="Data table">
    <tr><td></td><td></td><td></td><td></td><td></td></tr><tr><td></td><td></td><td></td><td></td><td></td></tr><tr><td></td><td></td><td></td><td></td><td></td></tr><tr><td></td><td></td><td></td><td></td><td></td></tr><tr><td></td><td></td><td></td><td></td><td></td></tr><tr><td></td><td></td><td></td><td></td><td></td></tr><tr><td></td><td></td><td></td><td></td><td></td></tr><tr><td></td><td></td><td></td><td></td><td></td></tr><tr><td></td><td></td><td></td><td></td><td></td></tr>
  </table>
  <div class="footer"><svg viewBox="0 0 293 42" preserveAspectRatio="none" aria-hidden="true"><rect y="8" width="293" height="34" fill="url(#fb)"/><path d="M0 0 H293 V10 Q220 14 146 24 Q73 14 0 10Z" fill="#fff"/><path d="M0 10 Q73 14 146 24 Q220 14 293 10" fill="none" stroke="#a9d6f7" stroke-width=".8"/></svg><span class="footer-url">www.harrowbyco.com</span><div class="footer-brand"><span class="brand-mark"></span><span class="brand-name">Harrowby &amp; Co</span></div><span class="footer-num">12</span></div>
</section>

<section class="slide c3 r5">
  <svg class="cover-bg" viewBox="0 0 293 223" aria-hidden="true">
    <rect width="293" height="223" fill="url(#gGrey)"/>
    <path d="M0 58 Q146 46 293 58 V150 L146 186 L0 150Z" fill="url(#gBand)"/>
    <path d="M0 58 Q146 46 293 58 V150 L146 186 L0 150Z" fill="url(#gShade)"/>
    <path d="M0 150 L146 186 L293 150" fill="none" stroke="#9fd0f5" stroke-width="1"/>
  </svg>
  <div class="cover-logo" style="top:18px">
    <div class="row"><span class="mark" style="width:7px;height:7px"></span><span class="name" style="font-size:8px">Harrowby &amp; Co</span></div>
    <div class="tag" style="font-size:2.8px">Strategy, Accounts &amp; Tax Advice</div>
  </div>
  <div class="cover-title" style="top:94px">THANK YOU VERY MUCH</div>
  <div class="cover-sub" style="top:113px">YOUR PRESENTATION TITLE HERE</div>
  <div class="cover-url">www.harrowbyco.com</div>
</section>

</body>
</html>
```